Social Media Graphics - ALL TEXT RK

We are looking for a series of social media graphics for Instagram (standard size 1:1 (1080x1080px) that are ALL TEXT. We want the following quotes below on each graphic; one quote per graphic. AND, In very small letters at the bottom of each graphic, add @RKMarlowLive

The look and feel of these graphics should be complimentary to the color palette attached below; but keep them simple. But the design is up to you; at the end of this document, I provided various samples of all text graphics that I like as examples.

Target Market(s)

women looking to lose weight

Industry/Entity Type

health and wellness

Colors
E54698
E96AAD
F1A4CE
F9D9EA
FCEFF6

Requirements
Must have
• the quotes in the document
Should not have
• no stock photography

```html
<!DOCTYPE html>
<html lang="en">
<head>
<meta charset="UTF-8">
<title>Stubborn Belly Fat Quote — RK</title>
<link href="https://fonts.googleapis.com/css2?family=Gilda+Display&display=swap" rel="stylesheet">
<style>
  :root {
    --bg: #ffffff;
    --ink: #cc0a6c;
    --highlight: #fdcfe6;
    --quote-mark: #efc6c8;
  }
  html, body {
    margin: 0;
    padding: 0;
    width: 1200px;
    height: 1200px;
    overflow: hidden;
    background: var(--bg);
  }
  .post {
    position: relative;
    width: 1200px;
    height: 1200px;
    background: var(--bg);
    font-family: "Gilda Display", Georgia, serif;
  }
  .quote-mark {
    position: absolute;
    left: 66px;
    top: 34px;
    font-size: 240px;
    line-height: 1;
    color: var(--quote-mark);
    font-family: "Gilda Display", Georgia, serif;
  }
  .highlights {
    position: absolute;
    left: 0;
    top: 0;
    width: 1200px;
    height: 1200px;
  }
  .highlights path { fill: var(--highlight); }
  .quote {
    position: absolute;
    left: 0;
    top: 223px;
    width: 1200px;
    margin: 0;
    text-align: center;
    color: var(--ink);
    font-size: 98px;
    line-height: 122px;
    font-weight: 400;
  }
  .quote span { display: block; }
  .handle {
    position: absolute;
    left: 0;
    width: 1200px;
    top: 1096px;
    text-align: center;
    color: var(--ink);
    font-size: 20px;
    letter-spacing: 1px;
    text-transform: uppercase;
  }
</style>
</head>
<body>
  <main class="post">
    <div class="quote-mark" aria-hidden="true">&#8221;</div>

    <svg class="highlights" viewBox="0 0 1200 1200" aria-hidden="true">
      <path d="M170 358 L1044 356 L1046 368 L1052 372 L1050 392 L1040 398 L1038 432 L1056 438 L1054 476 L1030 480 L146 478 L140 462 L142 436 L160 432 L160 402 L150 396 L150 372 L170 366 Z"/>
      <path d="M215 860 L942 858 L946 870 L940 878 L950 884 L948 904 L930 910 L928 926 L952 930 L950 958 L926 962 L200 960 L192 948 L196 926 L226 922 L228 910 L214 906 L212 884 L222 878 L212 870 Z"/>
    </svg>

    <h1 class="quote">
      <span>That</span>
      <span>stubborn belly fat</span>
      <span>isn't your fault -</span>
      <span>here's what</span>
      <span>no one</span>
      <span>tells you</span>
    </h1>

    <p class="handle">@RKMarlowLive</p>
  </main>
</body>
</html>
```